San Francisco Hotel - Fun Brochure Design

Hey!
I need a brochure that reflects my hotel's (Tindell's Motor Lodge) mid century modern feel while taking into account our excellent location in the Castro of San Francisco. I would like a fun brochure that is also sleek - on a rack of hotel brochures, I want ours to stand out, just like we do! Our building colors are quite bright - pinkish, blue and yellow - and are currently closely associated with us. Guests stay with us over and over again because of our wonderful location in the Castro (and very close to ZORA), our free parking (we're a motor lodge!), our free wireless internet and our reasonable rates. The final design should incorporate these things. In the coming year we will be going though renovations which will change our look (inside and out) and we will need completely new branding at that time as well.
LGTBQ, International travelers, 50+ year old couples
Wireless Internet

```html
<!DOCTYPE html>
<html lang="en">
<head>
<meta charset="utf-8">
<title>Tindell's Motor Lodge – Brochure</title>
<link rel="stylesheet" href="https://fonts.googleapis.com/css2?family=Merienda:wght@400;700&family=Source+Sans+3:wght@400;600;700&display=swap">
<style>
  :root {
    --red: #e2194b;
    --blue: #1f4fa0;
    --heading-blue: #2a55a6;
    --yellow: #f6c15a;
    --text: #111111;
    --white: #ffffff;
  }
  * { box-sizing: border-box; margin: 0; padding: 0; }
  html, body { width: 1200px; height: 926px; overflow: hidden; background: var(--white); }
  .brochure {
    position: relative; width: 1200px; height: 926px; overflow: hidden;
    background: var(--white);
    font-family: "Source Sans 3", Arial, sans-serif; color: var(--text);
  }
  .band-top { position: absolute; left: 0; top: 0; width: 1200px; height: 73px; background: var(--red); }
  .band-bottom { position: absolute; left: 0; top: 870px; width: 1200px; height: 56px; background: var(--blue); }

  .script { font-family: "Merienda", "Brush Script MT", cursive; }

  .photo { position: absolute; overflow: hidden; }
  .photo-caption {
    position: absolute; color: var(--white); font-family: "Merienda", cursive;
    font-size: 20px; text-shadow: 0 1px 3px rgba(0,0,0,.6); white-space: nowrap;
  }

  /* left panel */
  .sundeck {
    left: 0; top: 73px; width: 398px; height: 321px;
    background: linear-gradient(180deg, #7fa9d6 0%, #a7c3de 28%, #c9a857 45%, #b06a58 70%, #8a5447 100%);
  }
  .sundeck .photo-caption { left: 18px; top: 30px; font-size: 23px; line-height: 1.1; transform: rotate(-9deg); transform-origin: left top; }
  .intro { position: absolute; left: 30px; top: 430px; width: 336px; font-size: 16px; line-height: 30px; text-align: justify; }
  .intro p + p { margin-top: 28px; }
  .intro .lodge-name { color: var(--heading-blue); font-family: "Merienda", cursive; font-size: 18px; }
  .intro .castro { color: var(--red); }
  .call-box {
    position: absolute; left: 0; top: 719px; width: 366px; height: 110px;
    background: var(--yellow); text-align: center; padding-top: 12px;
  }
  .call-box .call-title { color: var(--red); font-family: "Merienda", cursive; font-size: 30px; line-height: 44px; }
  .call-box .call-phone { color: var(--red); font-weight: 700; font-size: 25px; line-height: 34px; letter-spacing: .5px; }

  /* center panel */
  .brand {
    position: absolute; left: 449px; top: 30px; width: 303px; height: 106px;
    background: var(--white); display: flex; align-items: center; justify-content: center; gap: 10px;
  }
  .brand-dot { width: 18px; height: 18px; border-radius: 50%; background: var(--yellow); flex: none; }
  .brand-name { font-family: "Merienda", cursive; font-weight: 700; font-size: 25px; color: var(--blue); white-space: nowrap; }

  .room-photo { border: 4px solid; }
  .room-photo .photo-caption { left: 14px; bottom: 8px; }
  .room-queens { left: 478px; top: 179px; width: 250px; height: 187px; border-color: var(--yellow);
    background: linear-gradient(160deg, #6b4a2e 0%, #a37a4c 40%, #c89a62 65%, #8a5a36 100%); }
  .room-queen { left: 474px; top: 409px; width: 251px; height: 187px; border-color: var(--blue);
    background: linear-gradient(170deg, #cfc29b 0%, #b9a47a 45%, #8b5a3a 75%, #6e4630 100%); }
  .room-king { left: 474px; top: 642px; width: 248px; height: 187px; border-color: var(--red);
    background: linear-gradient(175deg, #d86d67 0%, #e4877a 40%, #b8434a 72%, #8f2f3c 100%); }

  /* right panel */
  .section-title { position: absolute; left: 820px; width: 358px; text-align: center; color: var(--heading-blue); font-family: "Merienda", cursive; font-size: 31px; line-height: 44px; }
  .title-room { top: 102px; }
  .non-smoking { position: absolute; left: 820px; top: 161px; width: 358px; text-align: center; color: var(--red); font-weight: 700; font-size: 19px; }
  .feature-list { position: absolute; left: 820px; top: 202px; width: 358px; list-style: none; text-align: center; font-size: 17.5px; line-height: 25.7px; }
  .title-king { top: 415px; }
  .king-copy { position: absolute; left: 843px; top: 465px; width: 312px; font-size: 16px; line-height: 26px; text-align: justify; }
  .wireless { left: 850px; top: 607px; width: 297px; height: 222px;
    background: linear-gradient(150deg, #8c7a5c 0%, #a99470 40%, #6d5640 70%, #4a3a2c 100%); }
  .wireless .photo-caption { right: 14px; bottom: 12px; font-size: 21px; transform: rotate(-8deg); transform-origin: right bottom; }
</style>
</head>
<body>
<main class="brochure">
  <div class="band-top"></div>
  <div class="band-bottom"></div>

  <!-- left panel -->
  <div class="photo sundeck" role="img" aria-label="Rooftop sun deck with lounge chairs, a striped towel, potted flowers and city views">
    <span class="photo-caption">A Relaxing<br>Sun Deck</span>
  </div>
  <section class="intro">
    <p><span class="lodge-name">Tindell's Motor Lodge</span> is located in the <span class="castro">heart of the Castro</span>, and is surrounded by charming streets, unique restaurants and lively nightlife. We have a private sundeck where you will enjoy lovely views of the city.</p>
    <p>Public transportation is conveniently located just steps away from our front door.</p>
  </section>
  <div class="call-box">
    <div class="call-title">Call Us Now</div>
    <div class="call-phone">(415) 555-0147</div>
  </div>

  <!-- center panel -->
  <div class="brand">
    <span class="brand-dot"></span>
    <span class="brand-name">Tindell's Motor Lodge</span>
  </div>
  <div class="photo room-photo room-queens" role="img" aria-label="Guest room with two queen beds and bedside lamps">
    <span class="photo-caption">Two Queen's</span>
  </div>
  <div class="photo room-photo room-queen" role="img" aria-label="Guest room with a queen bed, framed prints and a desk chair">
    <span class="photo-caption">Queen</span>
  </div>
  <div class="photo room-photo room-king" role="img" aria-label="Guest room with a king bed under warm red lighting">
    <span class="photo-caption">King</span>
  </div>

  <!-- right panel -->
  <h2 class="section-title title-room">Room Features</h2>
  <div class="non-smoking">100% Non-Smoking Rooms</div>
  <ul class="feature-list">
    <li>private bathroom</li>
    <li>coffee maker</li>
    <li>refrigerator</li>
    <li>phone with voicemail</li>
    <li>free&nbsp; wireless internet</li>
    <li>free parking</li>
    <li>Tower Fan's</li>
  </ul>
  <h2 class="section-title title-king">King Bed Features</h2>
  <p class="king-copy">All of our King rooms include a 32” Flat Screen LCD TV. The King Deluxe and King Fireplace rooms are equipped with air conditioning.</p>
  <div class="photo wireless" role="img" aria-label="Room corner with an armchair, small table and a flower in a vase">
    <span class="photo-caption">Free Wireless!</span>
  </div>
</main>
</body>
</html>
```